Web Design for Small Healthcare Startup

Hello,

We are seeking a Website Design for a healthcare company focusing on mobile vaccinations, employee health and wellness services onsite at businesses, and consulting services relating to Healthcare Entities in WA state. Our company’s mission is to “To aid in a healthier workplace”. Brightpath Rovers will provide on-site wellness services to employers that simplify and streamline employee preventative health as well as onsite consulting services to help with compliance of Healthcare Entities.

We are seeking a Website Design for Brightpath Rovers, PLLC. Our company’s mission is to provide mobile health and wellness services to employers onsite at their businesses. These services include mobile vaccinations clinics for employees as well as wellness and health screenings. The company will also offer healtcare compliance consulting services for Healthcare Entities. The company was founded to bring these important healthcare services to businesses and keep employees healthy. Healthy employees are the cornerstone to a great business and we want to help orginazations achieve their goals of having a healthy productive workforce.

We are looking for a moderin website design that will need to be coded. We have attached our current logo design for reference as well as a brief questionare regarding our business for your information (not necessary to include all information). We would like something SEO friendly and easy to navigate.

Thank you!

Brightpath Rovers, PLLC

Target Market(s)

Small Businesses

Industry/Entity Type

Healthcare

Coding

Coded - Design and coding required

Number of Pages Required

1 page

Requirements
Nice to have
• SEO Friendly, Incorporate Logo

```html
<!DOCTYPE html>
<html lang="en">
<head>
<meta charset="utf-8">
<title>Brightpath Rovers, PLLC – To Aid in a Healthier Workplace</title>
<meta name="description" content="Brightpath Rovers, PLLC brings seamless, hassle-free on-site mobile vaccine clinics to your workplace.">
<link rel="stylesheet" href="https://fonts.googleapis.com/css2?family=Lato:wght@400;700;900&family=Ubuntu:wght@500;700&display=swap">
<style>
:root{
  --blue:#1b4f9c;
  --blue-deep:#0c3f8f;
  --purple:#a23d8f;
  --navy:#0f2a5c;
  --ink:#2b2b2b;
  --line:#c9c9c9;
  --white:#ffffff;
}
*{box-sizing:border-box;margin:0;padding:0}
html,body{width:1200px;height:3653px;overflow:hidden}
body{position:relative;background:var(--white);font-family:"Lato",sans-serif;color:var(--ink)}
a{text-decoration:none;color:inherit}
.abs{position:absolute}
.heading{font-family:"Ubuntu",sans-serif;font-weight:500;color:var(--blue);line-height:1.1}
.btn{position:absolute;display:flex;align-items:center;justify-content:center;border-radius:30px;font-weight:900;font-size:15px;color:var(--white);text-transform:uppercase;letter-spacing:-.2px;z-index:3}
.btn--purple{background:var(--purple)}
.btn--blue{background:var(--blue)}
.btn--white{background:var(--white);color:var(--blue)}

/* header */
.brand{position:absolute;display:flex;align-items:center;gap:8px;font-family:"Lato",sans-serif;font-weight:900;color:var(--blue)}
.brand__dot{width:18px;height:18px;border-radius:50%;background:var(--purple)}
.site-brand{left:142px;top:40px;font-size:22px}
.nav{position:absolute;top:46px;left:373px;display:flex;font-size:17px;color:#222}
.nav a{position:absolute;white-space:nowrap}
.nav .is-active{color:var(--blue)}
.header-phone{position:absolute;left:862px;top:38px;display:flex;align-items:center;gap:10px;color:var(--purple);font-weight:700;font-size:19px}

/* hero */
.hero-dots{left:64px;top:180px}
.hero-dots span{display:block;width:8px;height:8px;border-radius:50%;background:#d3d3d3;margin-bottom:14px}
.hero-dots span.on{background:var(--purple)}
.hero-title{left:149px;top:172px;font-size:51px;line-height:59px}
.hero-title em{font-style:normal;color:var(--purple)}
.hero-text{left:149px;top:368px;width:412px;font-size:14px;line-height:23px;text-align:justify}
.hero-photo{left:617px;top:119px;width:583px;height:464px;border-radius:300px 0 0 300px / 232px 0 0 232px;background:linear-gradient(135deg,#cfe0ea 0%,#e9d9c8 45%,#c9a98a 100%)}

/* about */
.about-art{left:92px;top:691px;width:454px;height:205px;border-radius:24px;background:linear-gradient(90deg,#f2e6f0,#e4ecf7)}
.about-title{left:586px;top:712px;font-size:48px}
.about-text{left:586px;top:792px;width:459px;font-size:13.5px;line-height:25.6px;text-align:justify}

/* services */
.services-band{left:0;top:1150px;width:730px;height:466px;background:linear-gradient(135deg,var(--blue-deep),#0a4aa6);border-radius:0 300px 300px 0 / 0 233px 233px 0}
.services-photo{left:662px;top:1150px;width:538px;height:466px;border-radius:250px 0 0 250px / 233px 0 0 233px;border:7px solid var(--white);border-right:0;background:linear-gradient(160deg,#e88a5a 0%,#b85b4a 45%,#5a3a3a 100%)}
.services-title{left:142px;top:1212px;font-size:50px;color:var(--white);z-index:2}
.services-text{left:142px;top:1291px;width:500px;font-size:13.2px;line-height:25.6px;letter-spacing:-.15px;color:var(--white);z-index:2}

/* pricing */
.center{left:0;width:1200px;text-align:center}
.pricing-title{top:1728px;font-size:50px}
.pricing-sub{top:1812px;font-size:15px;line-height:24px;color:#333}
.step-label{position:absolute;width:300px;text-align:center;font-family:"Ubuntu",sans-serif;font-weight:500;font-size:19px;line-height:23px;color:#1d1d1d}

/* schedule */
.schedule-band{left:17px;top:2365px;width:1166px;height:368px;border-radius:184px;background:linear-gradient(90deg,#a43a8c 0%,#7b46a3 45%,#2a54a8 80%,#0f4aa0 100%)}
.schedule-title{left:156px;top:2480px;font-size:50px;color:var(--white)}
.schedule-text{left:569px;top:2482px;width:490px;font-size:15px;line-height:24px;color:var(--white)}

/* contact */
.contact-title{top:2830px;font-size:50px}
.field{position:absolute;border:1px solid var(--line);background:var(--white);font-size:16px;color:#555;padding:18px 22px}

/* footer */
.footer{left:0;top:3331px;width:1200px;height:322px;background:var(--navy);color:var(--white)}
.footer-divider{position:absolute;top:44px;width:1px;height:185px;background:rgba(255,255,255,.18)}
.footer-heading{position:absolute;font-weight:700;font-size:16px;text-transform:uppercase}
.footer-list{position:absolute;left:511px;top:99px;list-style:none;font-size:12px}
.footer-list li{height:26.5px}
.footer-list li::before{content:"»";margin-right:14px}
.footer-input{position:absolute;left:796px;top:143px;width:235px;height:36px;border-radius:18px;background:var(--white);color:#666;font-size:11px;padding:11px 16px}
.copyright{position:absolute;left:0;width:1200px;top:278px;text-align:center;font-size:12px}
</style>
</head>
<body>

<header>
  <a class="brand site-brand" href="#home"><span class="brand__dot"></span>Brightpath Rovers</a>
  <nav class="nav">
    <a class="is-active" href="#home" style="left:0">Home</a>
    <a href="#about" style="left:81px">About</a>
    <a href="#services" style="left:163px">Services</a>
    <a href="#schedule" style="left:260px">Schedule Today</a>
    <a href="#pricing" style="left:407px">Pricing</a>
  </nav>
  <a class="header-phone" href="tel:+15550142290">
    <svg width="36" height="36" viewBox="0 0 36 36" aria-hidden="true"><circle cx="18" cy="18" r="16" fill="none" stroke="#1b4f9c" stroke-width="2.2"/><path d="M12.5 10.5l3 0 1.5 4-2 1.5c1 2.2 2.8 4 5 5l1.5-2 4 1.5v3c0 1-1 2-2 2-7 0-13-6-13-13 0-1 1-2 2-2z" fill="#1b4f9c"/></svg>
    +1 555 014 2290
  </a>
</header>

<main>
  <section id="home">
    <div class="abs hero-dots"><span></span><span></span><span class="on"></span><span></span></div>
    <h1 class="abs heading hero-title">To Aid in a<br><em>Healthier</em><br>Workplace</h1>
    <p class="abs hero-text">Brightpath Rovers specializes in providing seamless, hassle-free, on-site mobile vaccine clinics.No crowded waiting rooms, no long lines, no hassle!Specializing in workplace employee vaccine clinics.</p>
    <a class="btn btn--purple" href="#schedule" style="left:149px;top:467px;width:152px;height:54px">Reserve Now</a>
    <a class="btn btn--blue" href="#schedule" style="left:309px;top:467px;width:154px;height:54px">Calendar</a>
    <div class="abs hero-photo" role="img" aria-label="Photo of a woman with arms outstretched on a sunny beach"></div>
  </section>

  <section id="about">
    <div class="abs about-art" role="img" aria-label="Illustration of a mobile vaccine van with syringes"></div>
    <h2 class="abs heading about-title">About</h2>
    <p class="abs about-text">Brightpath Rovers, PLLC mission: Making the workplace a healthier place.To provide on-site wellness services to employers that simplify and streamline employee preventative health.Pharmacist owned and operated.Brightpath Rovers, PLLC was started by local, Washington state licensed pharmacist with over 15 years experience vaccinating patients. She is a highly skilled immunizer and enjoys interacting with patients while providing this important preventative health services. Her vaccination experience spans from individual patient vaccinations to large clinics during community outbreaks.</p>
    <a class="btn btn--purple" href="#about" style="left:586px;top:1031px;width:153px;height:54px">Read More</a>
  </section>

  <section id="services">
    <div class="abs services-band"></div>
    <div class="abs services-photo" role="img" aria-label="Photo of a person doing yoga beside a laptop at sunset in the city"></div>
    <h2 class="abs heading services-title">Services</h2>
    <p class="abs services-text">Brightpath Rovers will come to you! No crowded waiting rooms, no long lines, no hassle! Hassle-free, streamlining the vaccination process … provide this on-site service as part of your employee wellness package Serving employers who want to increase the health and Wellness of their workplace vaccines including seasonal flu, COVID, Pneumonia Ensure your employees and their families remain healthy this flu season. Host a flu shot clinic on site tohelp your employees get vaccinated. Provide this service as part of your employee Wellness benefits package.Brightpath Rovers specializes in providing seamless, hassle-free vaccine clinics.Don't wait for your employees to get their vaccines</p>
    <a class="btn btn--purple" href="#services" style="left:142px;top:1519px;width:153px;height:54px">Read More</a>
  </section>

  <section id="pricing">
    <h2 class="abs heading center pricing-title">Pricing</h2>
    <p class="abs center pricing-sub">Hassle-free, streamlining the vaccination process …<br>Submit this simple Vaccine Clinic Needs Questionnaire and Brightpath Rovers will do the rest.</p>

    <svg class="abs" style="left:130px;top:1920px" width="940" height="150" viewBox="0 0 940 150" aria-hidden="true">
      <defs><marker id="arrowhead" markerWidth="10" markerHeight="10" refX="6" refY="5" orient="auto"><path d="M0 0L10 5L0 10z" fill="#8a8a8a"/></marker></defs>
      <text x="0" y="120" font-family="Ubuntu,sans-serif" font-size="150" font-weight="500" fill="none" stroke="#1b4f9c" stroke-width="2.5">1</text>
      <circle cx="101" cy="73" r="63" fill="#fff" stroke="#1b4f9c" stroke-width="2.5"/>
      <circle cx="101" cy="73" r="46" fill="#a23d8f"/>
      <circle cx="108" cy="66" r="22" fill="none" stroke="#fff" stroke-width="3"/>
      <path d="M98 66l7 7 13-13" fill="none" stroke="#fff" stroke-width="3.5" stroke-linecap="round"/>
      <path d="M180 40q90-50 180 30" fill="none" stroke="#8a8a8a" stroke-width="2" stroke-dasharray="2 5" marker-end="url(#arrowhead)"/>
      <text x="365" y="120" font-family="Ubuntu,sans-serif" font-size="130" font-weight="500" fill="none" stroke="#1b4f9c" stroke-width="2.5">2</text>
      <circle cx="467" cy="73" r="63" fill="#fff" stroke="#1b4f9c" stroke-width="2.5"/>
      <rect x="440" y="45" width="54" height="48" rx="5" fill="none" stroke="#1b4f9c" stroke-width="2.5"/>
      <line x1="440" y1="58" x2="494" y2="58" stroke="#1b4f9c" stroke-width="2.5"/>
      <circle cx="492" cy="92" r="13" fill="#a23d8f"/>
      <path d="M486 92l4 4 8-8" fill="none" stroke="#fff" stroke-width="2.5"/>
      <path d="M555 100q80 50 175-5" fill="none" stroke="#8a8a8a" stroke-width="2" stroke-dasharray="2 5" marker-end="url(#arrowhead)"/>
      <text x="735" y="120" font-family="Ubuntu,sans-serif" font-size="130" font-weight="500" fill="none" stroke="#1b4f9c" stroke-width="2.5">3</text>
      <circle cx="837" cy="73" r="63" fill="#fff" stroke="#a23d8f" stroke-width="2.5"/>
      <circle cx="837" cy="55" r="10" fill="none" stroke="#1b4f9c" stroke-width="2.5"/>
      <circle cx="817" cy="88" r="10" fill="none" stroke="#1b4f9c" stroke-width="2.5"/>
      <circle cx="857" cy="88" r="10" fill="none" stroke="#1b4f9c" stroke-width="2.5"/>
    </svg>
    <p class="step-label" style="left:84px;top:2092px">Submit Vaccine<br>Clinic Needs<br>Questionnaire.</p>
    <p class="step-label" style="left:447px;top:2087px">Brightpath Rovers,<br>PLLC will contact you to<br>schedule on-site vaccine clinic</p>
    <p class="step-label" style="left:800px;top:2087px">Prepare your employees<br>for vaccine clinic day</p>
    <a class="btn btn--purple" href="tel:+15550142290" style="left:523px;top:2227px;width:152px;height:52px">Call Us Today</a>
  </section>

  <section id="schedule">
    <div class="abs schedule-band" role="img" aria-label="Purple and blue toned photo of a joyful woman outdoors"></div>
    <h2 class="abs heading schedule-title">Schedule Today</h2>
    <p class="abs schedule-text">Hassle-free, streamlining the vaccination process …<br>Submit this simple Vaccine Clinic Needs Questionnaire and Brightpath Rovers will do the rest.</p>
    <a class="btn btn--white" href="#contact" style="left:570px;top:2590px;width:176px;height:50px">Schedule Today</a>
  </section>

  <section id="contact">
    <h2 class="abs heading center contact-title">Get In Touch</h2>
    <div class="field" style="left:234px;top:2927px;width:360px;height:54px">First Name</div>
    <div class="field" style="left:605px;top:2927px;width:361px;height:54px">Last Name</div>
    <div class="field" style="left:234px;top:2992px;width:360px;height:54px">Email address</div>
    <div class="field" style="left:605px;top:2992px;width:361px;height:54px">Phone Number</div>
    <div class="field" style="left:234px;top:3057px;width:732px;height:114px">Message</div>
    <a class="btn btn--purple" href="#contact" style="left:523px;top:3206px;width:152px;height:53px">Submit</a>
  </section>
</main>

<footer class="abs footer">
  <svg class="abs" style="left:168px;top:61px" width="42" height="42" viewBox="0 0 36 36" aria-hidden="true"><circle cx="18" cy="18" r="16" fill="none" stroke="#fff" stroke-width="2"/><path d="M12.5 10.5l3 0 1.5 4-2 1.5c1 2.2 2.8 4 5 5l1.5-2 4 1.5v3c0 1-1 2-2 2-7 0-13-6-13-13 0-1 1-2 2-2z" fill="#fff"/></svg>
  <p class="abs" style="left:223px;top:58px;font-size:18px;font-weight:700">Contact Us</p>
  <p class="abs" style="left:223px;top:84px;font-size:24px;font-weight:700">1 555 014 2290</p>
  <p class="brand" style="left:168px;top:158px;font-size:19px;color:#5a7fd0"><span class="brand__dot"></span>Brightpath Rovers</p>
  <span class="footer-divider" style="left:444px"></span>
  <span class="footer-divider" style="left:732px"></span>
  <p class="footer-heading" style="left:511px;top:58px">What We Offer</p>
  <ul class="footer-list">
    <li>Home</li><li>About</li><li>Services</li><li>Schedule today</li><li>Pricing</li>
  </ul>
  <p class="footer-heading" style="left:796px;top:58px">Sign Up Newsletter</p>
  <p class="abs" style="left:796px;top:100px;font-size:11px">Lorem ipsum dolor sit ameonsectetur adip</p>
  <div class="footer-input">Enter Email</div>
  <a class="btn btn--purple" href="#contact" style="left:796px;top:191px;width:104px;height:35px;font-size:14px">Sign Up</a>
  <p class="copyright">© 2022 Brightpath Rovers LLC. All rights reserved &nbsp;|&nbsp; Privacy &nbsp;|&nbsp; Terms of Use</p>
</footer>

</body>
</html>
```